redesign of one of my packaging

Here I have a product packaging design that I have been using for a while on my e-commerce platform. I am planning on having multiple products very soon so I would like to have a packaging design that I will use for all my products that will represent my brand.
This is a zero-waste, eco-friendly/ sustainable product brand.
The packaging design that I use now needs to be redesign to match my brand a bit more.

-So in the file, you can find my current packaging design, All the text on the packaging is accurate the only thing is the brand name(logo) has been changed as well as the email address. I will put in the file the new brand name logo and the new email is "kestilo@fernwix.com" for detail ( Refer to pic #1)
(I am very open to the text I have. It doesn't have to be all there and if it is then the location of all the text is your choice)

- I currently have a designer that is modifying my packaging design. He is very good at designing and the design he sent me are nice but I need more different option to choose from. Here I will attach the design he got me so far. (refer to pic#2)

-For the design, I am very open to any kind of design. The only thing I want is to have the most of the background with the natural packaging color. For a sample of the color of my packaging (refer to pic#3)

-For the color... I would like for the design to have the 2 colors of my logo(blue and green)
but this is the first product of the line so I would not mind having the color of the logo different to have a better fit with the design of the packaging.

WHAT I LIKE:
-I like the concept of the bottom or top of the packaging when its a plain bright color
-I like when the packaging is not to busy in writing or shape
-I like to have an eco-friendly sign like the one on the current packaging
-I like little plain design but with nice little detail into it
-I like the color of my logo to be on the packaging(color of the logo can be modified)
-I like the contrast of the white on the natural color of the packaging
- I like the shade of all the item of the product on the bottom part of the current design( Not a need. Refer to pic#4)

What I like does, not mean that it needs to be on the design, I am very open to any design.

So I will also put in the files section some pictures of existing packaging design that I really like. Just to give you a good idea of what I want.
Those picture name will be (Design idea)

I will also put a picture of the actual product to help you with the design creation. The file name will be (Bamboo cutlery set)

Looking forward to seeing your design and I thank you in advance.

Theodore

```html
<!DOCTYPE html>
<html lang="en">
<head>
<meta charset="utf-8">
<title>Fernly Natural Bamboo Cutlery Set – Packaging Panels</title>
<link rel="stylesheet" href="https://fonts.googleapis.com/css2?family=Josefin+Sans:wght@300;400&family=Quicksand:wght@400;500&display=swap">
<style>
  :root {
    --kraft: #d2a67a;
    --kraft-shade: #c99c70;
    --teal: #07c9ac;
    --teal-deep: #0a9a80;
    --white: #ffffff;
    --leaf: rgba(255, 255, 255, 0.28);
    --page: #ffffff;
  }
  * { box-sizing: border-box; margin: 0; padding: 0; }
  html, body { width: 1200px; height: 1200px; overflow: hidden; background: var(--page); }
  .canvas { position: relative; width: 1200px; height: 1200px; }

  .dieline {
    position: absolute; left: 100px; top: 110px;
    display: flex; width: 1000px; height: 980px;
  }
  .panel {
    position: relative; width: 250px; height: 100%;
    background: var(--kraft); overflow: hidden;
  }
  .panel + .panel { border-left: 1px solid var(--kraft-shade); }

  .cap {
    height: 200px; background: var(--teal);
    display: flex; flex-direction: column; align-items: center; justify-content: center; gap: 14px;
  }
  .panel--side .cap { background: var(--teal-deep); }
  .brand-dot { width: 44px; height: 44px; border: 2px solid var(--white); border-radius: 50%; }
  .brand-name {
    font-family: "Josefin Sans", sans-serif; font-weight: 400;
    font-size: 30px; letter-spacing: 3px; color: var(--white);
  }

  /* front panel */
  .front-title {
    position: absolute; left: 40px; bottom: 200px;
    writing-mode: vertical-rl; transform: rotate(180deg);
    font-family: "Josefin Sans", sans-serif; font-weight: 300;
    font-size: 112px; letter-spacing: 14px; line-height: 1; color: var(--teal);
  }
  .front-subtitle {
    position: absolute; left: 158px; bottom: 205px;
    writing-mode: vertical-rl; transform: rotate(180deg);
    font-family: "Josefin Sans", sans-serif; font-weight: 300;
    font-size: 34px; line-height: 1; color: var(--white);
  }
  .leaf-sprig {
    position: absolute; left: 40px; right: 20px; bottom: 30px; height: 190px;
    border-radius: 60% 40% 55% 45%;
    background: radial-gradient(ellipse at center, var(--leaf), rgba(255,255,255,0) 70%);
  }

  /* copy panels */
  .copy { padding: 34px 24px 0 28px; color: var(--white); font-family: "Quicksand", sans-serif; }
  .copy-title { font-size: 22px; font-weight: 500; line-height: 1.25; margin-bottom: 50px; }
  .features { list-style: none; font-size: 14px; line-height: 1.3; }
  .features li { margin-bottom: 15px; padding-left: 10px; position: relative; }
  .features li::before { content: "•"; position: absolute; left: 0; }
  .maker { margin-top: 70px; font-size: 14px; line-height: 1.35; }
  .maker strong { font-weight: 500; }

  .specs { list-style: none; margin-top: -20px; }
  .spec { margin-bottom: 12px; }
  .spec-drawing {
    height: 30px; width: 150px; border-radius: 15px;
    background: linear-gradient(90deg, rgba(255,255,255,0.35), rgba(255,255,255,0.18));
  }
  .spec-drawing--case { height: 50px; border-radius: 8px; }
  .spec-drawing--thin { height: 14px; }
  .spec-size { font-size: 11px; margin-top: 4px; padding-left: 30px; }

  .eco-badge {
    position: absolute; left: 26px; bottom: 32px;
    width: 96px; height: 96px; border: 2px solid var(--white); border-radius: 50%;
  }
</style>
</head>
<body>
<main class="canvas">
  <div class="dieline">

    <section class="panel panel--front">
      <header class="cap"><span class="brand-dot"></span><span class="brand-name">FERNLY</span></header>
      <div class="leaf-sprig" role="img" aria-label="Faint white bamboo leaf sprig decoration"></div>
      <h1 class="front-title">FERNLY</h1>
      <p class="front-subtitle">Natural Bamboo Cutlery Set</p>
    </section>

    <section class="panel panel--side">
      <header class="cap"><span class="brand-dot"></span><span class="brand-name">FERNLY</span></header>
      <div class="copy">
        <h2 class="copy-title">100% Organic<br>Bamboo<br>Cutlery Set</h2>
        <ul class="features">
          <li>Super Sustainable</li>
          <li>Highly Durable</li>
          <li>Hand Finished</li>
          <li>Light Weight</li>
          <li>Easy to Use and Clean</li>
          <li>Made from<br>Natural Bamboo</li>
        </ul>
        <p class="maker">Manufactured by<br><strong>Fernly Goods</strong><br>kestilo@fernwix.com</p>
      </div>
      <div class="leaf-sprig" role="img" aria-label="Faint bamboo leaf sprig decoration"></div>
    </section>

    <section class="panel panel--specs">
      <header class="cap"><span class="brand-dot"></span><span class="brand-name">FERNLY</span></header>
      <div class="copy">
        <h2 class="copy-title">100% Organic<br>Bamboo<br>Cutlery Set</h2>
        <ul class="specs">
          <li class="spec"><div class="spec-drawing spec-drawing--case" role="img" aria-label="Line drawing of the carry case with dimensions A and B"></div><p class="spec-size">A: 9.05 inch &nbsp;B: 1.77 inch</p></li>
          <li class="spec"><div class="spec-drawing" role="img" aria-label="Line drawing of the spoon"></div><p class="spec-size">A: 7.9 inch &nbsp;B: 1.15 inch</p></li>
          <li class="spec"><div class="spec-drawing" role="img" aria-label="Line drawing of the fork"></div><p class="spec-size">A: 7.9 inch &nbsp;B: 1.15 inch</p></li>
          <li class="spec"><div class="spec-drawing" role="img" aria-label="Line drawing of the knife"></div><p class="spec-size">A: 7.9 inch &nbsp;B: 0.95 inch</p></li>
          <li class="spec"><div class="spec-drawing spec-drawing--thin" role="img" aria-label="Line drawing of the chopsticks"></div><p class="spec-size">A: 7.9 inch &nbsp;B: 0.40 inch</p></li>
          <li class="spec"><div class="spec-drawing spec-drawing--thin" role="img" aria-label="Line drawing of the straw and cleaning brush"></div><p class="spec-size">A: 7.9 inch &nbsp;B: 0.50 inch</p></li>
          <li class="spec"><div class="spec-drawing spec-drawing--thin" role="img" aria-label="Line drawing of the toothbrush"></div><p class="spec-size">A: 6.88 inch &nbsp;B: 0.70 inch</p></li>
        </ul>
      </div>
      <div class="eco-badge" aria-hidden="true"></div>
    </section>

    <section class="panel panel--front panel--side">
      <header class="cap"><span class="brand-dot"></span><span class="brand-name">FERNLY</span></header>
      <div class="leaf-sprig" role="img" aria-label="Faint bamboo leaf sprig decoration"></div>
      <h1 class="front-title">FERNLY</h1>
      <p class="front-subtitle">Natural Bamboo Cutlery Set</p>
    </section>

  </div>
</main>
</body>
</html>
```